Wedding Invitation and Logo

We would like an invitation and logo designed for our wedding on October 19, 2019 in Charlotte, NC. Our names are Tess and Hank, we met in school at Brindlewood Ridge University, and we got engaged at a fire tower which has a view down to the campus. You do not have to include these, but some ideas for the invitation design would be mountains, a fire tower, our initials, or the city. The wedding will be at 4:30 in the afternoon with a reception to follow. We do not need to list the families as there are four of them and that is too much info. The colors we would like to use are white, black, royal blue, and maybe silver. Do not feel obligated to use them all though.We would like the logo to include similar elements such as mountains, fire tower, or our initials(T and H). The logo can be a one color design as we may use it on our cake, as light filters to be displayed on the walls at our reception, or as an accent on name plates and stationery.We like simple, clean designs and our wedding will have a wintery theme (white linens, white chair covers, silver and royal blue accents, etc.).Things we do not want: snowflakes, flowers, polka dots, leaves, gold foil.Thank you!

Font styles to use
Serif
Script

Requirements
Must have
• Some combination of white, black, royal blue, optionally silver.
Nice to have
• Mountains, fire tower, our initials (T and H), wintry theme (no snowflakes)
Should not have
• Snowflakes, flowers, polka dots, leaves, gold foil

```html
<!DOCTYPE html>
<html lang="en">
<head>
<meta charset="utf-8">
<title>Tess &amp; Hank — Wedding Invitation</title>
<link rel="stylesheet" href="https://fonts.googleapis.com/css2?family=Montserrat:wght@400;500&family=Cinzel:wght@500&family=Cormorant+Garamond:wght@500;600&display=swap">
<style>
  :root {
    --backdrop: #e8eaee;
    --navy: #262a5a;
    --silver: #d6d8de;
    --silver-ink: #9b9ea8;
    --paper: #ffffff;
  }
  * { margin: 0; padding: 0; box-sizing: border-box; }
  html, body {
    width: 1200px; height: 1200px; overflow: hidden;
    background: var(--backdrop);
  }
  .invitation {
    position: absolute; left: 210px; top: 54px;
    width: 780px; height: 1092px;
    box-shadow: 0 10px 30px rgba(30, 34, 70, 0.18);
  }
  .invitation__frame { position: absolute; inset: 0; }
  .facet { stroke: var(--silver); stroke-width: 3; stroke-linejoin: round; }
  .facet--dark { fill: url(#washDark); }
  .facet--mid { fill: url(#washMid); }
  .facet--light { fill: url(#washLight); }
  .invitation__panel { fill: var(--paper); stroke: var(--silver); stroke-width: 3; }
  .arc-line {
    font-family: "Montserrat", sans-serif; font-size: 25px; font-weight: 500;
    letter-spacing: 3px; fill: var(--navy);
  }
  .copy {
    position: absolute; left: 120px; width: 540px; text-align: center; color: var(--navy);
  }
  .announce {
    top: 178px; font-family: "Montserrat", sans-serif; font-size: 25px; font-weight: 500;
    letter-spacing: 3px; line-height: 1.2;
  }
  .tower {
    position: absolute; left: 352px; top: 335px; width: 76px; height: 250px;
    background: linear-gradient(180deg, #5a5e86 0%, #8f93b0 100%);
    clip-path: polygon(38% 0, 62% 0, 100% 100%, 0 100%);
  }
  .couple {
    top: 622px; font-family: "Cinzel", serif; font-size: 58px; font-weight: 500;
    letter-spacing: 3px; line-height: 1.2; color: var(--silver-ink);
  }
  .venue {
    top: 712px; font-family: "Montserrat", sans-serif; font-size: 23px; font-weight: 500;
    letter-spacing: 2.5px; line-height: 1.2;
  }
  .when {
    top: 752px; font-family: "Cormorant Garamond", serif; font-size: 46px; font-weight: 600;
    letter-spacing: 5px; line-height: 1.2; font-variant-numeric: lining-nums;
  }
  .when small { font-size: 30px; letter-spacing: 2px; }
  .reception {
    top: 890px; font-family: "Cormorant Garamond", serif; font-size: 22px; font-weight: 600;
    letter-spacing: 2.5px; line-height: 1.2;
  }
</style>
</head>
<body>
  <main class="invitation">
    <svg class="invitation__frame" width="780" height="1092" viewBox="0 0 780 1092" xmlns="http://www.w3.org/2000/svg">
      <defs>
        <linearGradient id="washDark" x1="0" y1="0" x2="1" y2="1">
          <stop offset="0" stop-color="#2f3362"/><stop offset="1" stop-color="#4c5080"/>
        </linearGradient>
        <linearGradient id="washMid" x1="0" y1="0" x2="1" y2="1">
          <stop offset="0" stop-color="#666a8c"/><stop offset="1" stop-color="#8b8ea9"/>
        </linearGradient>
        <linearGradient id="washLight" x1="0" y1="0" x2="1" y2="1">
          <stop offset="0" stop-color="#b8bbcb"/><stop offset="1" stop-color="#9699b1"/>
        </linearGradient>
        <path id="celebrateArc" d="M 193 572 A 210 210 0 1 1 587 572"/>
      </defs>
      <g class="frame-facets">
        <polygon class="facet facet--light" points="0,0 230,0 120,110"/>
        <polygon class="facet facet--mid" points="230,0 400,110 120,110"/>
        <polygon class="facet facet--dark" points="230,0 520,0 400,110"/>
        <polygon class="facet facet--light" points="520,0 660,110 400,110"/>
        <polygon class="facet facet--dark" points="520,0 780,0 660,110"/>
        <polygon class="facet facet--mid" points="780,0 780,300 660,110"/>
        <polygon class="facet facet--dark" points="780,300 660,500 660,110"/>
        <polygon class="facet facet--light" points="780,300 780,700 660,500"/>
        <polygon class="facet facet--mid" points="780,700 660,970 660,500"/>
        <polygon class="facet facet--light" points="780,700 780,1092 660,970"/>
        <polygon class="facet facet--dark" points="780,1092 560,1092 660,970"/>
        <polygon class="facet facet--light" points="560,1092 400,970 660,970"/>
        <polygon class="facet facet--mid" points="560,1092 250,1092 400,970"/>
        <polygon class="facet facet--dark" points="250,1092 120,970 400,970"/>
        <polygon class="facet facet--light" points="250,1092 0,1092 120,970"/>
        <polygon class="facet facet--mid" points="0,1092 0,760 120,970"/>
        <polygon class="facet facet--dark" points="0,760 120,600 120,970"/>
        <polygon class="facet facet--light" points="0,760 0,380 120,600"/>
        <polygon class="facet facet--mid" points="0,380 120,300 120,600"/>
        <polygon class="facet facet--dark" points="0,380 120,110 120,300"/>
        <polygon class="facet facet--light" points="0,0 120,110 0,380"/>
      </g>
      <rect class="invitation__panel" x="120" y="110" width="540" height="860"/>
      <text class="arc-line"><textPath href="#celebrateArc" startOffset="50%" text-anchor="middle">YOU ARE INVITED TO CELEBRATE WITH</textPath></text>
    </svg>

    <p class="copy announce">WE ARE<br>GETTING MARRIED!</p>
    <div class="tower" role="img" aria-label="Line illustration of a fire lookout tower"></div>
    <h1 class="copy couple">TESS &amp; HANK</h1>
    <p class="copy venue">AT CHARLOTTE, NORTH CAROLINA</p>
    <p class="copy when">10 | 19 | 2019 | 4:30 <small>PM</small></p>
    <p class="copy reception">RECEPTION TO FOLLOW</p>
  </main>
</body>
</html>
```